K9 Orbit needs a business card designed

We need a business card designed for K9 Orbit, an expansion of K9 Systems Pty Ltd (www.k9systems.com.au)

We provide high quality professional services for the Australian space industry. Our clients include the Southern Launch Bureau and companies working in the space industry. We identify people with space related skills both locally and internationally who are then contracted by clients to create products and support space launch activities.

Colours to be used:
- Navy blue #000080
- Rocket metallic #8A7F8D
- Platinum #E5E4E2
- Black #000000
- White #FFFFFF

*Front of the card*
I have attached our K9 Orbit logo, which needs to be the main item on the card. The 'Space' text should be placed to the right of the 'K9' part rather than below, similar to the attached K9 Systems card, which this card should match.

If subtext is included, however, it should read ‘Labour Hire • Consultancy • Project Delivery’ rather than the ‘Design • Build • Test • Maintain’ of the K9 Systems card.

A black background (rather than blue background in the K9 Systems card) might be good, with a white pattern as in the K9 Systems card. If colour is used, the logo should be in its standard colours (as provided for the K9 Orbit logo).

*Back of the card*
Include a smaller K9 Orbit logo on the back.

We need the following details for K9 Orbit personnel (as a template for entry):
- Name
- Company Position
- Mobile Number
- Email
- Office Address
- Include the K9 Orbit website: www.k9orbit.com.au

Overall, we'd like to see a design that communicates the adventure of space, professional integrity, and customer service. We look forward to seeing what you can come up with.

Target Market(s)

We provide high quality professional services for the Australian space industry. Our clients include the Southern Launch Bureau and companies working in the space industry.

Contact Information for Business Card

- Name
- Company Position
- Mobile Number
- Email
- Office Address

Requirements
Must have
• See project description.

```html
<!DOCTYPE html>
<html lang="en">
<head>
<meta charset="utf-8">
<title>K9 Orbit Business Card</title>
<link href="https://fonts.googleapis.com/css2?family=Roboto:wght@400;500;700&display=swap" rel="stylesheet">
<style>
  :root {
    --navy: #27286f;
    --metal: #8a7f8d;
    --white: #ffffff;
    --stage: #666464;
    --shadow: #1b1b1b;
  }
  * { margin: 0; padding: 0; box-sizing: border-box; }
  html, body {
    width: 1200px; height: 801px; overflow: hidden;
    background: var(--stage);
    font-family: "Roboto", Arial, sans-serif;
  }
  .card {
    position: absolute; top: 274px;
    width: 443px; height: 263px;
    overflow: hidden;
    box-shadow: 2px 2px 0 var(--shadow);
  }
  .card--front { left: 153px; background: var(--white); }
  .card--back { left: 625px; background: var(--navy); }

  .band {
    position: absolute; left: 0; right: 0; top: 96px; bottom: 0;
    background: linear-gradient(180deg, var(--white) 0%, var(--metal) 12%, var(--navy) 32%, var(--navy) 100%);
  }

  .brand {
    position: absolute; display: flex; align-items: center;
    font-weight: 500; white-space: nowrap; letter-spacing: 0;
  }
  .brand__dot { border-radius: 50%; flex: none; }

  .card--front .brand { left: 24px; top: 34px; color: var(--navy); font-size: 26px; }
  .card--front .brand__dot { width: 16px; height: 16px; background: var(--navy); margin-right: 10px; }

  .back-lockup {
    position: absolute; left: 0; right: 0; top: 88px;
    display: flex; flex-direction: column; align-items: center; gap: 12px;
  }
  .card--back .brand { position: static; color: var(--white); font-size: 34px; }
  .card--back .brand__dot { width: 20px; height: 20px; background: var(--white); margin-right: 12px; }
  .tagline { color: var(--white); font-size: 11px; white-space: nowrap; }

  .details {
    position: absolute; right: 26px; top: 116px;
    color: var(--white); text-align: right;
  }
  .details__name { font-size: 17px; font-weight: 700; line-height: 19px; }
  .details__role { font-size: 13px; line-height: 16px; margin-bottom: 6px; }
  .contact { font-size: 12.5px; line-height: 16px; display: flex; justify-content: flex-end; align-items: center; gap: 4px; }
  .contact svg { width: 10px; height: 10px; flex: none; }
  .address { font-size: 12.5px; line-height: 16px; margin-top: 5px; }
</style>
</head>
<body>

<section class="card card--front" aria-label="Card front">
  <div class="band" role="img" aria-label="Decorative navy wave band"></div>

  <div class="brand"><span class="brand__dot"></span>K9 Orbit</div>

  <div class="details">
    <p class="details__name">MARCUS HALE</p>
    <p class="details__role">Managing Director</p>
    <p class="contact">044-987 654 321
      <svg viewBox="0 0 10 10" aria-hidden="true"><rect x="2" y="0.5" width="6" height="9" rx="1" fill="none" stroke="currentColor"/><circle cx="5" cy="8" r="0.6" fill="currentColor"/></svg>
    </p>
    <p class="contact">info@mailhost.com
      <svg viewBox="0 0 10 10" aria-hidden="true"><rect x="0.5" y="2" width="9" height="6.5" fill="none" stroke="currentColor"/><path d="M0.5,2 L5,6 L9.5,2" fill="none" stroke="currentColor"/></svg>
    </p>
    <p class="contact">www.k9orbit.com.au
      <svg viewBox="0 0 10 10" aria-hidden="true"><circle cx="5" cy="5" r="4.5" fill="none" stroke="currentColor"/><ellipse cx="5" cy="5" rx="2" ry="4.5" fill="none" stroke="currentColor"/><path d="M0.5,5 H9.5" stroke="currentColor" stroke-width="0.7"/></svg>
    </p>
    <p class="address">421, Address line goes here<br>45452,Country Name</p>
  </div>
</section>

<section class="card card--back" aria-label="Card back">
  <div class="back-lockup">
    <div class="brand"><span class="brand__dot"></span>K9 Orbit</div>
    <p class="tagline">Labour Hire • Consultancy • Project Delivery</p>
  </div>
</section>

</body>
</html>
```